Business Card Design For Office Furniture Clearance Company

Kestrel Office Clearance - our company name pretty much explains what we do, we clear offices for high end clients, mainly plc's and large international companies.

We require a nice looking business card that displays professionalism but without being too serious.

It would be nice to see just a little more than a conventional boring business card, make sure you add some flare.

Industry/Entity Type

Office Furniture

Contact Information for Business Card

CARD 1

Tom Pardew
Director
tom@kestrelofficeclearance.co.uk
m: 07700 513928

t: 01632 419063
www.kestrelofficeclearance.co.uk

Kestrel Office Clearance
Unit K4 B
3-7 Ferndale Lane
Harrowfield
Ashbury Vale
ZZ9 4QX

Free office clearances… no better deal than that.

CARD 2

Henry Walbrook
Director
henry@kestrelofficeclearance.co.uk
m: 07700 628157

t: 01632 419063

Kestrel Office Clearance
Unit K4 B
3-7 Ferndale Lane
Harrowfield
Ashbury Vale
ZZ9 4QX

Font styles to use
Sans Serif

Requirements
Must have
• A white background - as we have a blue logo.
Nice to have
• Nice use of the logo - play around with this and dissect it.

```html
<!DOCTYPE html>
<html lang="en">
<head>
<meta charset="utf-8">
<title>Kestrel Office Clearance — Business Cards</title>
<link rel="stylesheet" href="https://fonts.googleapis.com/css2?family=Arimo:wght@400;700&family=Lora:ital,wght@1,500&display=swap">
<style>
  :root {
    --blue: #1b80c4;
    --blue-deep: #0f5e98;
    --ink: #1c1c1c;
    --rule: #444444;
    --white: #ffffff;
    --backdrop: #e9ebee;
  }
  * { box-sizing: border-box; margin: 0; padding: 0; }
  html, body {
    width: 1200px; height: 900px; overflow: hidden;
    background: var(--backdrop);
    font-family: "Arimo", Arial, sans-serif;
  }
  .stage {
    position: relative; width: 1200px; height: 900px;
    display: flex; align-items: center; justify-content: center; gap: 40px;
  }
  .card {
    position: relative; width: 540px; height: 349px;
    overflow: hidden;
    box-shadow: 0 10px 28px rgba(0,0,0,.18);
  }

  /* Front */
  .card-front { background: var(--blue); color: var(--white); }
  .city-photo {
    position: absolute; left: 0; top: 0; width: 62%; height: 100%;
    background: linear-gradient(90deg, rgba(15,94,152,.55) 0%, rgba(20,100,160,.35) 60%, rgba(27,128,196,0) 100%);
  }
  .front-brand {
    position: absolute; left: 44px; top: 84px;
    display: flex; align-items: center; gap: 24px;
  }
  .brand-dot {
    width: 120px; height: 120px; border-radius: 50%;
    background: var(--white); flex: none;
  }
  .brand-name {
    font-weight: 700; font-size: 34px; line-height: 1.04;
    color: var(--white); text-transform: uppercase; letter-spacing: .5px;
  }
  .tagline {
    position: absolute; left: 44px; right: 30px; bottom: 38px;
    font-family: "Lora", Georgia, serif; font-style: italic; font-weight: 500;
    font-size: 18px; letter-spacing: .3px; color: var(--white);
    white-space: nowrap;
  }

  /* Back */
  .card-back { background: var(--white); color: var(--ink); }
  .holder { position: absolute; left: 36px; top: 32px; }
  .holder-name { font-size: 27px; font-weight: 400; letter-spacing: .2px; }
  .holder-role { font-size: 13px; color: var(--blue); margin-top: 4px; }
  .back-mark {
    position: absolute; right: 40px; top: 34px;
    width: 128px; height: 128px; border-radius: 50%; background: var(--blue);
  }
  .divider {
    position: absolute; left: 36px; right: 36px; top: 178px;
    height: 1px; background: var(--rule);
  }
  .contacts {
    position: absolute; left: 36px; top: 196px;
    list-style: none; font-size: 13px; line-height: 1;
  }
  .contacts li { display: flex; align-items: center; gap: 8px; margin-bottom: 7px; }
  .contacts svg { width: 12px; height: 12px; flex: none; }
  .address {
    position: absolute; right: 36px; top: 196px;
    text-align: right; font-size: 13px; line-height: 1.32; font-style: normal;
  }
</style>
</head>
<body>
<main class="stage">

  <section class="card card-front" aria-label="Business card front">
    <div class="city-photo" role="img" aria-label="Faded blue-toned city skyline photograph"></div>
    <div class="front-brand">
      <span class="brand-dot"></span>
      <span class="brand-name">Kestrel<br>Office<br>Clearance</span>
    </div>
    <p class="tagline">Free office clearances… no better deal than that.</p>
  </section>

  <section class="card card-back" aria-label="Business card back">
    <div class="holder">
      <h1 class="holder-name">Tom Pardew</h1>
      <p class="holder-role">Director</p>
    </div>
    <span class="back-mark"></span>
    <div class="divider"></div>

    <ul class="contacts">
      <li>
        <svg viewBox="0 0 12 12" aria-hidden="true"><rect width="12" height="12" rx="2" fill="#1b80c4"/><rect x="4" y="2" width="4" height="8" rx="1" fill="none" stroke="#fff" stroke-width="1"/></svg>
        07700 513928
      </li>
      <li>
        <svg viewBox="0 0 12 12" aria-hidden="true"><rect width="12" height="12" rx="2" fill="#1b80c4"/><path d="M3 3.5c0 3 2.5 5.5 5.5 5.5l.8-1.4-1.6-.9-.7.7C5.8 7 5 6.2 4.6 5l.7-.7-.9-1.6z" fill="#fff"/></svg>
        01632 419063
      </li>
      <li>
        <svg viewBox="0 0 12 12" aria-hidden="true"><rect width="12" height="12" rx="2" fill="#1b80c4"/><rect x="2.5" y="3.5" width="7" height="5" fill="none" stroke="#fff" stroke-width="1"/><path d="M2.5 3.5 6 6.5l3.5-3" fill="none" stroke="#fff" stroke-width="1"/></svg>
        tom@kestrelofficeclearance.co.uk
      </li>
      <li>
        <svg viewBox="0 0 12 12" aria-hidden="true"><rect width="12" height="12" rx="2" fill="#1b80c4"/><circle cx="6" cy="6" r="3.5" fill="none" stroke="#fff" stroke-width="1"/><path d="M2.5 6h7M6 2.5v7" stroke="#fff" stroke-width=".8"/></svg>
        www.kestrelofficeclearance.co.uk
      </li>
    </ul>

    <address class="address">
      Kestrel Office Clearance<br>
      Unit K4 B<br>
      3-7 Ferndale Lane<br>
      Harrowfield<br>
      Ashbury Vale<br>
      ZZ9 4QX
    </address>
  </section>

</main>
</body>
</html>
```